A QUIET AMBER PRIMER ON RANKS

subtitle: AN INTRO TO SEARCH ENGINE OPTIMIZATION
background: white
dimensions: 1562x2500

Target Market(s)

Marketing professionals

Industry/Entity Type

Digital Marketing

Font styles to use
Sans Serif

Colors
ffffff
1b1b1b
3176b5

Requirements
Should not have
• Images or graphics

```html
<!DOCTYPE html>
<html lang="en">
<head>
<meta charset="utf-8">
<title>A Quiet Amber Primer on Ranks</title>
<link rel="stylesheet" href="https://fonts.googleapis.com/css2?family=Archivo+Black&display=swap">
<style>
  :root {
    --paper: #ffffff;
    --ink: #1b1b1b;
    --accent: #3176b5;
    --author-ink: #0a0a0a;
  }
  html, body {
    margin: 0;
    padding: 0;
    width: 764px;
    height: 1200px;
    overflow: hidden;
    background: var(--paper);
  }
  .book-cover {
    display: block;
    width: 764px;
    height: 1200px;
    background: var(--paper);
  }
  .cover-title {
    font-family: "Archivo Black", "Arial Black", sans-serif;
    fill: var(--ink);
  }
  .cover-title .title-accent {
    fill: var(--accent);
  }
  .cover-subtitle {
    font-family: "Archivo Black", "Arial Black", sans-serif;
    fill: var(--ink);
  }
  .cover-author {
    font-family: "Archivo Black", "Arial Black", sans-serif;
    fill: var(--author-ink);
  }
</style>
</head>
<body>
  <svg class="book-cover" viewBox="0 0 764 1200" xmlns="http://www.w3.org/2000/svg" role="img" aria-label="A Quiet Amber Primer on Ranks: An intro to search engine optimization, by Daniel Forsythe">
    <g class="cover-title">
      <text class="title-line title-line--first" x="37" y="157" font-size="150" textLength="690" lengthAdjust="spacingAndGlyphs">A QUIET</text>
      <text class="title-line title-line--second" x="37" y="370" font-size="257" textLength="690" lengthAdjust="spacingAndGlyphs">AMBER</text>
      <text class="title-line title-line--third" x="37" y="597" font-size="307" textLength="690" lengthAdjust="spacingAndGlyphs">PRIMER</text>
      <text class="title-line title-line--fourth" x="37" y="789" font-size="257" textLength="690" lengthAdjust="spacingAndGlyphs">ON <tspan class="title-accent">RANKS</tspan></text>
    </g>
    <text class="cover-subtitle" x="382" y="872" font-size="26" text-anchor="middle" textLength="640" lengthAdjust="spacingAndGlyphs">AN INTRO TO SEARCH ENGINE OPTIMIZATION</text>
    <text class="cover-author" x="382" y="1145" font-size="60" text-anchor="middle" textLength="509" lengthAdjust="spacingAndGlyphs">DANIEL FORSYTHE</text>
  </svg>
</body>
</html>
```